Business Card Design Project

We need a business card design for a management consultancy focused on financial innovation and digital money, run by experts from the Financial Services, Telecoms and Money Transfer industries.
Our products include services such as Mobile Payments, Mobile Money, Digital Wallets, Online Payments, Branchless Banking and more. We work with regulatory information, business plans, financial modelling, strategic planning, new products functional specification, new technologies evaluation, etc.
See company logo attached.
We would like to see 2 versions: one in portuguese and one in english (regarding data information). You can see below information needed (whenever there is a difference between the two versions, the first one is in english and the second one in portuguese).

Name
Position
Phone/ Tel: ++55-11-xxxx-xxxx
Cell/ Cel: ++55-11-9 xxxx-xxxx
Dr. Tavares Lobato Av., 318 - Tower II - 16th floor / Avenida Dr. Tavares Lobato, 318 - Torre II - 16o. andar
São Paulo - SP
01327-118 - Brazil/ 01327-118 - Brasil

Target Market(s)

Audience: C-level executives from banks, credit card companies, acquirers, IT developers, retailers

Industry/Entity Type

Financial

Requirements
Must have
• Must use the logo and information above. Front must have white background. Back side should have only logo.
Nice to have
• Back should be in another colour but if it seems too exxagerated, maintain back in white also.
Should not have
• Do not add other illustrations to the business card.

```html
<!DOCTYPE html>
<html lang="en">
<head>
<meta charset="utf-8">
<title>R Hartwell Management Consulting – Business Card</title>
<link rel="stylesheet" href="https://fonts.googleapis.com/css2?family=Crimson+Text:wght@400&display=swap">
<style>
  :root {
    --card-white: #ffffff;
    --band-grey: #c1c2c4;
    --rule-grey: #8a8b8d;
    --brand-navy: #1f3a70;
    --text-black: #1a1a1a;
  }
  html, body {
    margin: 0;
    padding: 0;
    width: 1200px;
    height: 667px;
    overflow: hidden;
    background: var(--card-white);
  }
  .card {
    position: relative;
    width: 1200px;
    height: 667px;
    background: var(--card-white);
    font-family: "Crimson Text", Georgia, serif;
  }
  .brand {
    position: absolute;
    left: 58px;
    top: 68px;
    display: flex;
    align-items: flex-end;
    gap: 18px;
  }
  .brand-square {
    width: 116px;
    height: 116px;
    background: var(--brand-navy);
  }
  .brand-name {
    color: var(--brand-navy);
    font-weight: 400;
    text-transform: uppercase;
    line-height: 1;
    margin: 0;
    padding-bottom: 2px;
  }
  .brand-name-main {
    display: block;
    font-size: 56px;
    letter-spacing: 2px;
  }
  .brand-name-sub {
    display: block;
    font-size: 25px;
    letter-spacing: 1.5px;
    margin-top: 4px;
  }
  .contact-band {
    position: absolute;
    left: 0;
    top: 333px;
    width: 1200px;
    height: 334px;
    background: var(--band-grey);
    border-top: 1px solid var(--rule-grey);
    box-sizing: border-box;
  }
  .contact-details {
    position: absolute;
    left: 53px;
    top: 38px;
    margin: 0;
    padding: 0;
    list-style: none;
    color: var(--text-black);
    font-size: 23.5px;
    line-height: 32px;
  }
</style>
</head>
<body>
  <div class="card">
    <header class="brand">
      <div class="brand-square" aria-hidden="true"></div>
      <h1 class="brand-name">
        <span class="brand-name-main">R Hartwell</span>
        <span class="brand-name-sub">Management Consulting</span>
      </h1>
    </header>
    <section class="contact-band">
      <ul class="contact-details">
        <li>Name</li>
        <li>Position</li>
        <li>Phone/ Tel: ++55-11-xxxx-xxxx</li>
        <li>Cell/ Cel: ++55-11-9 xxxx-xxxx</li>
        <li>Dr. Tavares Lobato Av., 318 - Tower II - 16th floor / Avenida Dr.</li>
        <li>Tavares Lobato, 318 - Torre II - 16o. andar</li>
        <li>São Paulo - SP</li>
        <li>01327-118 - Brazil/ 01327-118 - Brasil</li>
      </ul>
    </section>
  </div>
</body>
</html>
```